Morvela Aesthetic Doctor

I require an elegant, luxurious looking business card for my aesthetic business. I am a doctor and that will set me aside from competitors. I am planning to provide home and spa based treatments to clients with high expectations. I have attached my logo.

```html
<!DOCTYPE html>
<html lang="en">
<head>
<meta charset="utf-8">
<title>Morvela Aesthetic Doctor – Business Card</title>
<link href="https://fonts.googleapis.com/css2?family=Cinzel:wght@400;600&family=Open+Sans:wght@400;600;700&display=swap" rel="stylesheet">
<style>
  :root {
    --bg: #e9ecf0;
    --card: #ffffff;
    --ink-grey: #8d8f93;
    --ink-dark: #6f7175;
    --blue: #2f9fd0;
    --blue-deep: #3a6fc3;
    --cyan: #45b6df;
    --stripe: #c9cbcf;
  }
  * { box-sizing: border-box; margin: 0; padding: 0; }
  html, body { width: 1200px; height: 900px; overflow: hidden; }
  body {
    background: var(--bg);
    font-family: "Open Sans", Arial, sans-serif;
    position: relative;
  }
  .card {
    position: absolute;
    left: 260px;
    width: 680px;
    height: 388px;
    background: var(--card);
    overflow: hidden;
    box-shadow: 0 6px 18px rgba(40, 50, 70, .18);
  }
  .card--front { top: 42px; }
  .card--back { top: 470px; }
  .card__swoosh { position: absolute; inset: 0; width: 100%; height: 100%; }

  .brand {
    position: absolute;
    display: flex;
    align-items: center;
    gap: 12px;
    color: var(--blue);
    font-family: "Cinzel", serif;
    font-weight: 400;
  }
  .brand__dot {
    width: 46px; height: 46px;
    border-radius: 50%;
    background: var(--cyan);
    flex: none;
  }
  .brand__text { line-height: 1; }
  .brand__name { display: block; font-size: 40px; letter-spacing: 1px; }
  .brand__tag { display: block; font-size: 15px; letter-spacing: 2px; margin-top: 4px; }

  .front .brand { top: 48px; right: 40px; }

  .doctor {
    position: absolute;
    left: 40px;
    top: 136px;
  }
  .doctor__name {
    font-family: "Cinzel", serif;
    font-weight: 400;
    font-size: 30px;
    color: var(--ink-grey);
    letter-spacing: 1px;
  }
  .doctor__cred {
    font-size: 14px;
    color: var(--blue);
    line-height: 1.45;
    margin-top: 6px;
  }

  .contact {
    position: absolute;
    left: 420px;
    top: 200px;
    list-style: none;
  }
  .contact__item {
    display: flex;
    align-items: center;
    gap: 14px;
    height: 24px;
    font-size: 14px;
    font-weight: 600;
    color: var(--ink-dark);
  }
  .contact__icon { width: 16px; height: 16px; flex: none; }
  .social { display: flex; gap: 18px; margin-top: 10px; }
  .social__square { width: 20px; height: 20px; background: var(--cyan); border-radius: 3px; }

  .services__title {
    position: absolute;
    left: 300px;
    top: 28px;
    font-family: "Cinzel", serif;
    font-weight: 400;
    font-size: 30px;
    color: var(--ink-grey);
    text-decoration: underline;
    text-underline-offset: 6px;
    text-decoration-thickness: 2px;
  }
  .services__list {
    position: absolute;
    list-style: none;
    font-size: 17px;
    font-weight: 700;
    color: var(--ink-grey);
  }
  .services__list--left { left: 150px; top: 92px; }
  .services__list--right { left: 430px; top: 150px; }
  .services__list li {
    display: flex; align-items: center; gap: 14px; height: 30px;
  }
  .services__list li::before {
    content: ""; width: 11px; height: 11px; border-radius: 50%;
    background: radial-gradient(circle at 35% 35%, #bfe6f6, var(--cyan));
  }
  .tagline {
    position: absolute;
    left: 150px;
    top: 218px;
    display: flex;
    align-items: center;
    gap: 14px;
    font-family: "Cinzel", serif;
    font-weight: 600;
    font-size: 17px;
    color: var(--blue);
    letter-spacing: 1px;
  }
  .tagline__rule { width: 36px; height: 2px; background: var(--blue); }
  .back .brand { left: 420px; top: 254px; }
  .back .brand__dot { width: 36px; height: 36px; }
  .back .brand__name { font-size: 30px; }
  .back .brand__tag { font-size: 12px; }
</style>
</head>
<body>

<section class="card card--front front">
  <svg class="card__swoosh" viewBox="0 0 680 388" preserveAspectRatio="none" aria-hidden="true">
    <defs>
      <linearGradient id="frontBand" x1="0" y1="0" x2="1" y2="1">
        <stop offset="0" stop-color="#3fb0dc"/>
        <stop offset=".45" stop-color="#9fd4f0"/>
        <stop offset="1" stop-color="#3a6fc3"/>
      </linearGradient>
    </defs>
    <path d="M0,218 C140,300 390,350 680,345" fill="none" stroke="#c9cbcf" stroke-width="9"/>
    <path d="M0,236 C150,318 400,362 680,360 L680,388 L0,388 Z" fill="url(#frontBand)"/>
  </svg>

  <div class="brand">
    <span class="brand__dot"></span>
    <span class="brand__text">
      <span class="brand__name">MORVELA</span>
      <span class="brand__tag">AESTHETIC DOCTOR</span>
    </span>
  </div>

  <div class="doctor">
    <h1 class="doctor__name">DR ELISE MARWOOD</h1>
    <p class="doctor__cred">MRCPCH MD<br>Australasian Diploma of Aesthetic Medicine</p>
  </div>

  <ul class="contact">
    <li class="contact__item">
      <svg class="contact__icon" viewBox="0 0 16 16"><path d="M4 1 L6.5 4.5 L5 6.2 C6 8.2 7.8 10 9.8 11 L11.5 9.5 L15 12 L13.2 14.8 C7 14.5 1.5 9 1.2 2.8 Z" fill="none" stroke="#2f9fd0" stroke-width="1.3"/></svg>
      0800 555 013
    </li>
    <li class="contact__item">
      <svg class="contact__icon" viewBox="0 0 16 16"><rect x="1" y="3" width="14" height="10" fill="none" stroke="#2f9fd0" stroke-width="1.3"/><path d="M1 3 L8 9 L15 3" fill="none" stroke="#2f9fd0" stroke-width="1.3"/></svg>
      elise@morvela.co.nz
    </li>
    <li class="contact__item">
      <svg class="contact__icon" viewBox="0 0 16 16"><circle cx="8" cy="8" r="6.5" fill="none" stroke="#2f9fd0" stroke-width="1.2"/><ellipse cx="8" cy="8" rx="3" ry="6.5" fill="none" stroke="#2f9fd0" stroke-width="1.1"/><path d="M1.5 8 H14.5" stroke="#2f9fd0" stroke-width="1.1"/></svg>
      www.morvela.co.nz
    </li>
    <li class="social">
      <span class="social__square"></span>
      <span class="social__square"></span>
    </li>
  </ul>
</section>

<section class="card card--back back">
  <svg class="card__swoosh" viewBox="0 0 680 388" preserveAspectRatio="none" aria-hidden="true">
    <defs>
      <linearGradient id="backBand" x1="0" y1="0" x2="1" y2="1">
        <stop offset="0" stop-color="#3fb0dc"/>
        <stop offset=".45" stop-color="#9fd4f0"/>
        <stop offset="1" stop-color="#3a6fc3"/>
      </linearGradient>
    </defs>
    <path d="M0,262 C150,330 400,358 680,352" fill="none" stroke="#c9cbcf" stroke-width="8"/>
    <path d="M0,280 C150,345 400,372 680,366 L680,388 L0,388 Z" fill="url(#backBand)"/>
  </svg>

  <h2 class="services__title">OUR SERVICES:</h2>
  <ul class="services__list services__list--left">
    <li>Dermal injectables</li>
    <li>Microneedling</li>
    <li>Excessive sweating</li>
  </ul>
  <ul class="services__list services__list--right">
    <li>Plasma facials</li>
    <li>Skin boosters</li>
  </ul>

  <p class="tagline"><span class="tagline__rule"></span>HOME AND SPA BASED TREATMENTS<span class="tagline__rule"></span></p>

  <div class="brand">
    <span class="brand__dot"></span>
    <span class="brand__text">
      <span class="brand__name">MORVELA</span>
      <span class="brand__tag">AESTHETIC DOCTOR</span>
    </span>
  </div>
</section>

</body>
</html>
```